Satchel & Compass needs new business card design

I need a new business card design. I'm looking for out-of-the-box design which represents the freedom of being a location independent entrepreneur.
I offer coaching, retreats and trips.
I would like to see designs with and without the photo.
Colors I use are black (#000000), green (#25A796) and brown (#D7C38C)
Website satchelandcompass.com

Target Market(s)

location independent entrepreneurs, digital nomads, people looking to swap the 9 to 5 for a lifestyle business

Industry/Entity Type

Business

Contact Information for Business Card

Petra Varga
Your Lifestyle Business Coach, Retreat & Trip Leader
http://satchelandcompass.com
hello@satchelandcompass.com
Live a life you don't need a holiday from

Font styles to use
Serif
Sans Serif

Requirements
Must have
• One side should contain only the logo. I would also consider having the "Live a life you don't need a holiday from" on that side too (depending on how it looks)
• Please show both sides on the designs.

```html
<!DOCTYPE html>
<html lang="en">
<head>
<meta charset="utf-8">
<title>Satchel &amp; Compass — Business Card</title>
<link rel="stylesheet" href="https://fonts.googleapis.com/css2?family=Roboto:wght@400;500&family=Lora:ital,wght@1,500&display=swap">
<style>
  :root {
    --bg: #e4e5e7;
    --brand-green: #25a796;
    --brand-black: #000000;
    --paper: #ffffff;
    --photo-light: #b7c08a;
    --photo-mid: #6f8a4c;
    --photo-dark: #3f5a33;
    --shadow: rgba(0, 0, 0, 0.18);
  }
  * { box-sizing: border-box; margin: 0; padding: 0; }
  html, body { width: 1200px; height: 800px; overflow: hidden; }
  body {
    background: var(--bg);
    font-family: "Roboto", Arial, sans-serif;
    position: relative;
  }
  .card {
    position: absolute;
    top: 245px;
    width: 540px;
    height: 310px;
    border-radius: 4px;
    box-shadow: 0 10px 28px var(--shadow);
    overflow: hidden;
  }
  /* Front: contact side */
  .card--front {
    left: 40px;
    background: var(--brand-green);
    color: var(--paper);
  }
  .card--front .wordmark {
    position: absolute;
    left: 30px;
    top: 26px;
    font-size: 30px;
    font-weight: 500;
    letter-spacing: 0.5px;
  }
  .contact {
    position: absolute;
    left: 30px;
    top: 96px;
    width: 250px;
  }
  .contact__name { font-size: 19px; font-weight: 500; margin-bottom: 4px; }
  .contact__role { font-size: 12.5px; line-height: 1.35; margin-bottom: 14px; }
  .contact__list { list-style: none; font-size: 12.5px; line-height: 1.55; }
  .contact__list li { display: flex; align-items: center; gap: 8px; }
  .contact__list svg { width: 12px; height: 12px; flex: none; }
  .tagline {
    position: absolute;
    left: 30px;
    bottom: 30px;
    font-family: "Lora", Georgia, serif;
    font-style: italic;
    font-weight: 500;
    font-size: 14px;
  }
  .photo {
    position: absolute;
    right: 24px;
    top: 112px;
    width: 226px;
    height: 178px;
    border-radius: 10px;
    background: radial-gradient(circle at 40% 55%, var(--photo-light), var(--photo-mid) 55%, var(--photo-dark));
  }
  /* Back: logo side */
  .card--back {
    left: 620px;
    background: var(--paper);
    color: var(--brand-black);
  }
  .card--back .wordmark {
    position: absolute;
    left: 0; right: 0;
    top: 108px;
    text-align: center;
    font-size: 40px;
    font-weight: 500;
    letter-spacing: 0.5px;
  }
  .card--back .web {
    position: absolute;
    left: 0; right: 0;
    top: 210px;
    text-align: center;
    font-family: "Lora", Georgia, serif;
    font-style: italic;
    font-weight: 500;
    font-size: 13px;
  }
</style>
</head>
<body>
  <section class="card card--front" aria-label="Card front">
    <div class="wordmark">Satchel &amp; Compass</div>
    <div class="contact">
      <p class="contact__name">Petra Varga</p>
      <p class="contact__role">Your Lifestyle Business Coach<br>Retreat &amp; Trip Leader</p>
      <ul class="contact__list">
        <li>
          <svg viewBox="0 0 12 12" aria-hidden="true"><path d="M2.5 1 L4.5 1 L5.2 3.4 L4 4.3 C4.6 5.7 6.3 7.4 7.7 8 L8.6 6.8 L11 7.5 L11 9.5 C11 10.3 10.3 11 9.5 11 C5 11 1 7 1 2.5 C1 1.7 1.7 1 2.5 1 Z" fill="currentColor"/></svg>
          0412-7780-3291
        </li>
        <li>
          <svg viewBox="0 0 12 12" aria-hidden="true"><rect x="0.5" y="2" width="11" height="8" rx="1" fill="currentColor"/><path d="M1 2.5 L6 6.5 L11 2.5" stroke="#25a796" stroke-width="1" fill="none"/></svg>
          hello@satchelandcompass.com
        </li>
        <li>
          <svg viewBox="0 0 12 12" aria-hidden="true"><rect x="1" y="1.5" width="10" height="7" rx="0.8" fill="none" stroke="currentColor" stroke-width="1.2"/><rect x="4" y="9.5" width="4" height="1.2" fill="currentColor"/></svg>
          www.satchelandcompass.com
        </li>
      </ul>
    </div>
    <p class="tagline">Live a life you don't need a holiday from</p>
    <div class="photo" role="img" aria-label="Photo of the coach sitting on a wooden fence among trees, holding a small sign"></div>
  </section>

  <section class="card card--back" aria-label="Card back">
    <div class="wordmark">Satchel &amp; Compass</div>
    <p class="web">www.satchelandcompass.com</p>
  </section>
</body>
</html>
```